TALRENO Business Cards

We require a business card for our company that provides IT consulting services. We already have a logo that needs to be used on the card. We want a clean professional looking design that incorporates our colours. Our main focus is providing managed services to business, which involves us looking after all of their IT requirements including managing servers/networks, projects, and procurement.

Industry/Entity Type

Information Technology

Requirements
Must have
• our logo, contact information, name, title, phone numbers

```html
<!DOCTYPE html>
<html lang="en">
<head>
<meta charset="utf-8">
<title>TALRENO Business Cards</title>
<link href="https://fonts.googleapis.com/css2?family=Montserrat:wght@600&family=Open+Sans:wght@400;600&display=swap" rel="stylesheet">
<style>
  :root {
    --backdrop: #3a3a37;
    --card: #161616;
    --brand-blue: #1c8fd6;
    --text-white: #f4f4f4;
  }
  html, body {
    margin: 0;
    padding: 0;
    width: 1200px;
    height: 824px;
    overflow: hidden;
    background: var(--backdrop);
  }
  .canvas {
    position: relative;
    width: 1200px;
    height: 824px;
  }
  .card {
    position: absolute;
    width: 500px;
    height: 286px;
    background: var(--card);
    border-radius: 3px;
    box-shadow: 0 10px 30px rgba(0,0,0,0.45);
  }
  .card-front { left: 70px; top: 110px; }
  .card-back { left: 630px; top: 420px; }

  .brand {
    display: flex;
    align-items: center;
    gap: 10px;
    color: var(--brand-blue);
    font-family: "Open Sans", sans-serif;
    font-weight: 600;
    letter-spacing: 3px;
  }
  .brand-dot {
    border-radius: 50%;
    background: var(--brand-blue);
  }
  .card-front .brand {
    position: absolute;
    left: 0; right: 0; top: 104px;
    justify-content: center;
    font-size: 44px;
  }
  .card-front .brand-dot { width: 30px; height: 30px; }
  .front-website {
    position: absolute;
    left: 0; right: 0; top: 178px;
    text-align: center;
    color: var(--brand-blue);
    font-family: "Open Sans", sans-serif;
    font-size: 13px;
    letter-spacing: 2px;
  }

  .card-back .brand {
    position: absolute;
    left: 34px; top: 92px;
    font-size: 30px;
  }
  .card-back .brand-dot { width: 22px; height: 22px; }
  .contact-block {
    position: absolute;
    left: 262px; top: 84px;
    font-family: "Open Sans", sans-serif;
  }
  .person-name {
    margin: 0;
    color: var(--text-white);
    font-family: "Montserrat", sans-serif;
    font-weight: 600;
    font-size: 20px;
    letter-spacing: 0.5px;
  }
  .person-title {
    margin: 0 0 14px;
    color: var(--brand-blue);
    font-size: 13px;
    letter-spacing: 1px;
  }
  .contact-list { list-style: none; margin: 0; padding: 0; }
  .contact-list li {
    display: flex;
    align-items: center;
    gap: 9px;
    color: var(--text-white);
    font-size: 13.5px;
    line-height: 24px;
  }
  .contact-list svg { width: 13px; height: 13px; fill: var(--brand-blue); flex: none; }
</style>
</head>
<body>
<main class="canvas">
  <section class="card card-front">
    <div class="brand"><span class="brand-dot"></span>TALRENO</div>
    <div class="front-website">www.yourwebsite.com</div>
  </section>

  <section class="card card-back">
    <div class="brand"><span class="brand-dot"></span>TALRENO</div>
    <div class="contact-block">
      <h1 class="person-name">YOUR NAME</h1>
      <p class="person-title">JOB TITLE</p>
      <ul class="contact-list">
        <li>
          <svg viewBox="0 0 24 24"><path d="M6.6 10.8a15.1 15.1 0 0 0 6.6 6.6l2.2-2.2c.3-.3.7-.4 1-.2 1.1.4 2.3.6 3.6.6.6 0 1 .4 1 1V20c0 .6-.4 1-1 1A17 17 0 0 1 3 4c0-.6.4-1 1-1h3.5c.6 0 1 .4 1 1 0 1.3.2 2.5.6 3.6.1.3 0 .7-.2 1z"/></svg>
          000 000 0000
        </li>
        <li>
          <svg viewBox="0 0 24 24"><path d="M2 5h20v14H2z M2 5l10 8 10-8" fill="var(--brand-blue)"/><path d="M2 6l10 7 10-7" fill="none" stroke="#161616" stroke-width="1.6"/></svg>
          youremail@xyz.com
        </li>
        <li>
          <svg viewBox="0 0 24 24"><circle cx="12" cy="12" r="9.5" fill="none" stroke="var(--brand-blue)" stroke-width="2"/><path d="M2.5 12h19M12 2.5c-5 5-5 14 0 19M12 2.5c5 5 5 14 0 19" fill="none" stroke="var(--brand-blue)" stroke-width="1.6"/></svg>
          www.yourwebsite.com
        </li>
        <li>
          <svg viewBox="0 0 24 24"><path d="M12 2a7 7 0 0 0-7 7c0 5.2 7 13 7 13s7-7.8 7-13a7 7 0 0 0-7-7zm0 9.5A2.5 2.5 0 1 1 12 6.5a2.5 2.5 0 0 1 0 5z"/></svg>
          0000. Anywhere, City, ST 0000
        </li>
      </ul>
    </div>
  </section>
</main>
</body>
</html>
```